Australian home builder requires inclusion list design

We require two inclusions list's flyers to showcase our two different inclusions. The design of the flyer is to reinforce professionalism and quality.
One inclusions list for each specification (i.e Tarn and Cornerway)

Target Market(s)

Home Buyers aged 25 - 55

Industry/Entity Type

Home Builder

Other font styles liked:
• Harabara

```html
<!DOCTYPE html>
<html lang="en">
<head>
<meta charset="utf-8">
<title>Tarn Inclusions</title>
<link href="https://fonts.googleapis.com/css2?family=Raleway:wght@300;400;600&family=Roboto:wght@400;700&display=swap" rel="stylesheet">
<style>
:root{
  --bg:#7fc6a7;
  --paper:#f4f4f4;
  --green:#2f9a3c;
  --leaf-dark:#1f3a1c;
  --leaf-mid:#4a7a3e;
  --band:#2b2b2b;
  --ink:#1e1e1e;
  --text:#3a3a3a;
}
*{box-sizing:border-box;margin:0;padding:0}
html,body{width:1200px;height:927px;overflow:hidden;background:var(--bg)}
.flyer{position:absolute;left:290px;top:25px;width:620px;height:877px;overflow:hidden;background:var(--paper);box-shadow:0 12px 30px rgba(0,0,0,.18);font-family:"Roboto",Arial,sans-serif;color:var(--text);display:flex;flex-direction:column}
.header{position:relative;height:178px;flex:none;background:linear-gradient(120deg,var(--leaf-dark) 0%,var(--leaf-mid) 55%,#6f9a5e 80%,#3c6331 100%)}
.brand{position:absolute;left:38px;top:66px;display:flex;align-items:center;gap:10px}
.brand-mark{width:22px;height:22px;background:var(--green)}
.brand-name{font-family:"Raleway",sans-serif;font-weight:600;font-size:24px;color:#ffffff;letter-spacing:.5px}
.tagline-band{flex:none;height:22px;background:var(--band);color:#fff;font-family:"Raleway",sans-serif;font-size:10px;letter-spacing:7px;text-align:center;line-height:22px}
.title{flex:none;margin-top:24px;text-align:center;font-family:"Raleway",sans-serif;font-weight:300;font-size:38px;line-height:46px;letter-spacing:9px;color:var(--green)}
.title .bracket{color:var(--ink)}
.columns{flex:none;margin:22px 44px 0;display:grid;grid-template-columns:1fr 1fr 1fr;gap:20px}
.section-title{font-family:"Raleway",sans-serif;font-weight:400;font-size:14px;letter-spacing:1px;color:var(--green);margin:0 0 10px}
.section-title.spaced{margin-top:20px}
.item{margin-bottom:10px;font-size:9px;line-height:1.3}
.item h3{font-size:10.5px;font-weight:700;color:var(--ink);margin-bottom:1px}
.item p+p{margin-top:6px}
.footer{flex:none;margin:14px 60px 0;border-top:1px solid var(--ink);border-bottom:1px solid var(--ink);padding:14px 0 16px;text-align:center;color:var(--ink)}
.footer .company{font-family:"Raleway",sans-serif;font-weight:600;font-size:13px;letter-spacing:4px}
.footer .company span{color:var(--green)}
.footer p{font-size:10px;letter-spacing:2px;margin-top:5px}
</style>
</head>
<body>
<main class="flyer">
  <div class="header" role="img" aria-label="Green tinted photograph of leafy garden plants beside a timber deck">
    <div class="brand"><span class="brand-mark"></span><span class="brand-name">Harbourline Homes</span></div>
  </div>
  <div class="tagline-band">LIVING THE DREAM!</div>

  <h1 class="title"><span class="bracket">[</span>TARN INCLUSIONS<span class="bracket">]</span></h1>

  <div class="columns">
    <section>
      <h2 class="section-title">EXTERNAL FEATURE</h2>
      <div class="item"><h3>External Wall Constructions</h3><p>Smooth Cement rendered block construction</p></div>
      <div class="item"><h3>Metal Roofing</h3><p>Ironleaf custom orb roofing from the standard Ironleaf range.</p></div>
      <div class="item"><h3>Fascia &amp; Gutter</h3><p>Ironleaf fascia and gutter from the standard Ironleaf range</p></div>
      <div class="item"><h3>Windows</h3><p>Powdercoat Aluminium windows and doors with grey glass</p></div>
      <div class="item"><h3>Window Screens</h3><p>Flyscreens to all aluminium windows and security grill to sliding glass doors and garage external access door (where applicable)</p></div>
      <div class="item"><h3>Entrance Doors</h3><p>Selection of Ashby Doors from the Harbourline Homes Tarn Range</p></div>
      <div class="item"><h3>Entrance Door Furniture</h3><p>Holloway Keylock or Holloway K2 Series 450mm Oblong Pull Handle Entrance Set</p></div>
      <div class="item"><h3>External Cladding</h3><p>Lightweight cladding to outer walls where indicated (refer design plans)</p></div>
    </section>

    <section>
      <div class="item"><h3>Driveway</h3><p>Exposed Aggregate driveway as shown on design plans</p></div>
      <div class="item"><h3>Clothesline</h3><p>Fernline wall hung clothesline</p><p>Exposed Aggregate Drying Court as per design plans</p></div>
      <div class="item"><h3>Mailbox</h3><p>Choice of Mailbox from Harbourline Homes Tarn Range</p></div>
      <h2 class="section-title spaced">SITE-SPECIFIC COSTS</h2>
      <div class="item"><h3>Site Survey</h3><p>Soil Testing, Wind Classification and Contour Plan</p></div>
      <div class="item"><h3>Site Levels</h3><p>Site Cut/Fill, maximum 400mm cut and 400mm fill</p></div>
      <div class="item"><h3>Sanitary Services</h3><p>Storm Water, Sewer, and water connections as per Coral Bay Regional Council Requirements</p></div>
      <div class="item"><h3>Utility Connections</h3><p>Power connections to Voltra requirements and FibreNet Lead in Cabling</p></div>
    </section>

    <section>
      <h2 class="section-title">KITCHEN</h2>
      <div class="item"><h3>Oven</h3><p>Kestrel Multifunction Stainless Steel Oven</p></div>
      <div class="item"><h3>Cooktop</h3><p>Kestrel 60cm Ceramic Cooktop</p></div>
      <div class="item"><h3>Rangehood</h3><p>Kestrel 60cm slide-out rangehood or Kestrel 90cm canopy</p></div>
      <div class="item"><h3>Sink</h3><p>Brookmere Essential 1 ½ Bowl Sink</p></div>
      <div class="item"><h3>Sink Mixer</h3><p>Ripple Sink mixer</p></div>
      <div class="item"><h3>Dishwasher</h3><p>Kestrel Freestanding stainless look Dishwasher</p></div>
      <div class="item"><h3>Splashback</h3><p>Ceramic Tiles above all benchtop surfaces up to the top cupboard height</p></div>
      <div class="item"><h3>Cabinetry</h3><p>Veneerco Finish with the inclusion of 2 x Pot Draws and 1 x bank of cutlery draws.</p><p>Laminated Top cupboards (refer to design plans)</p></div>
      <div class="item"><h3>Benchtops</h3><p>Choice of Square Edge or Bullnose Laminated Benchtops</p></div>
    </section>
  </div>

  <footer class="footer">
    <div class="company">HARBOURLINE <span>HOMES</span> NQ</div>
    <p>24 Wattlebrook Ave, Seaview QLD 4700</p>
    <p>CALL (07) 4000 1234</p>
  </footer>
</main>
</body>
</html>
```